Restaurant menu design

I need a menu for a restaurant in Spain.
It has to be bohemian but modern. We need something romantic and elegant.
The restaurant is elegant with good food and an excellent reputation. It is also modern at the same time.
The restaurant is superbly decorated and very chick so we need something "class" to fit in with the surroundings.
The size of the document must be 325 mm in high and 245 mm as a maximum and preferably made in indesign.

Reason: Thank you all for your designs.
So far all your designs are ok but it isn´t what we are looking for. Most of the designs are too loaded, too many colors and too much decoration.

Target Market(s)

Adults of various age groups and different nationalities mostly European.

Industry/Entity Type

Restaurant

Requirements
Must have
• The menu must have two interior pages with the text as in the document attached.It must be easily legible.
Nice to have
• See what kind of menus they use in important restaurants in places like Paris, see what designs are in trend, but Not necessarily doing the same style if it doesn’t fit in with the description above.
Should not have
• Nothing old fashioned.

```html
<!DOCTYPE html>
<html lang="es">
<head>
<meta charset="utf-8">
<title>Carta — Entradas, Pescados al Grill, Especial Niños</title>
<link rel="stylesheet" href="https://fonts.googleapis.com/css2?family=Parisienne&family=Tinos:ital@1&display=swap">
<style>
  :root {
    --ink-light: #f4efe9;
    --title-red: #c42a2e;
    --top-warm-1: #5c544c;
    --top-warm-2: #8a8178;
    --top-warm-3: #3f3833;
    --bottom-dark-1: #2a211b;
    --bottom-dark-2: #4a3b30;
    --bottom-dark-3: #1c1612;
  }
  * { margin: 0; padding: 0; box-sizing: border-box; }
  html, body { width: 904px; height: 1200px; overflow: hidden; background: #1c1612; }
  .menu-page {
    position: relative;
    width: 904px;
    height: 1200px;
    overflow: hidden;
    font-family: "Tinos", "Times New Roman", serif;
    font-style: italic;
    color: var(--ink-light);
  }
  .backdrop { position: absolute; left: 0; width: 904px; }
  .backdrop--dining-table {
    top: 0; height: 654px;
    background:
      radial-gradient(ellipse at 50% 45%, var(--top-warm-2) 0%, transparent 60%),
      linear-gradient(180deg, var(--top-warm-1) 0%, var(--top-warm-2) 45%, var(--top-warm-3) 100%);
  }
  .backdrop--restaurant-interior {
    top: 654px; height: 546px;
    background:
      radial-gradient(ellipse at 20% 40%, #5a4538 0%, transparent 55%),
      linear-gradient(180deg, var(--bottom-dark-2) 0%, var(--bottom-dark-1) 50%, var(--bottom-dark-3) 100%);
  }
  .menu-section { position: absolute; left: 0; width: 890px; text-align: center; }
  .section-title {
    font-family: "Parisienne", cursive;
    font-style: normal;
    font-weight: 400;
    font-size: 38px;
    color: var(--title-red);
    line-height: 1;
    margin-bottom: 24px;
  }
  .dish-list { list-style: none; }
  .dish { font-size: 15.5px; line-height: 26.2px; white-space: nowrap; }
  .dish-price { margin-left: 20px; font-size: 13.5px; }
  .menu-section--starters { top: 96px; }
  .menu-section--grill { top: 645px; }
  .menu-section--grill .dish { line-height: 26.5px; }
  .menu-section--kids { top: 1008px; }
  .menu-section--kids .section-title { margin-bottom: 28px; }
</style>
</head>
<body>
<main class="menu-page">
  <div class="backdrop backdrop--dining-table" role="img" aria-label="Photograph of a set restaurant table with wine glasses, a bottle of red wine, oil and vinegar cruets and pink lilies, with faint floral swirl ornaments"></div>
  <div class="backdrop backdrop--restaurant-interior" role="img" aria-label="Dim photograph of the restaurant dining room with pink flowers and glasses on laid tables, with faint floral swirl ornaments"></div>

  <section class="menu-section menu-section--starters">
    <h2 class="section-title">Entradas</h2>
    <ul class="dish-list">
      <li class="dish">Ensalada La Violette. Lechuga, tomate.<span class="dish-price">7,75 €</span></li>
      <li class="dish">Ensalada Caprese (Tomate y Mozzarella).<span class="dish-price">7,75 €</span></li>
      <li class="dish">Escarola al Queso de Cabra con Bacon.<span class="dish-price">6,75 €</span></li>
      <li class="dish">Cocktail de Gambas, Langostinos y Aguacate.<span class="dish-price">7,50 €</span></li>
      <li class="dish">La Sopa de Pescado.<span class="dish-price">8,25 €</span></li>
      <li class="dish">Crema de Espárragos Trigueros y Calabacín.<span class="dish-price">5,95 €</span></li>
      <li class="dish">Carpaccio de Ternera.<span class="dish-price">11,50 €</span></li>
      <li class="dish">Carpaccio de Salmón al Eneldo.<span class="dish-price">9,75 €</span></li>
      <li class="dish">Carpaccio de Atún.<span class="dish-price">13,95 €</span></li>
      <li class="dish">Melón con Jamón Ibérico.<span class="dish-price">9,25 €</span></li>
      <li class="dish">Parrillada de Verduras.<span class="dish-price">7,95 €</span></li>
      <li class="dish">Parrillada de Verduras Gratinada al Queso de Cabra.<span class="dish-price">8,95 €</span></li>
      <li class="dish">Gambas Roja de la Bahia.<span class="dish-price">12,95 €</span></li>
    </ul>
  </section>

  <section class="menu-section menu-section--grill">
    <h2 class="section-title">Pescados al Grill</h2>
    <ul class="dish-list">
      <li class="dish">Lubina al Hinojo.<span class="dish-price">15,50 €</span></li>
      <li class="dish">Lubina Fileteada y su Salsa Rústica con Berenjena.<span class="dish-price">18,50 €</span></li>
      <li class="dish">Filete de Rodaballo y su Salsa de Marisco.<span class="dish-price">17,25 €</span></li>
      <li class="dish">Dorada del Mediterráneo.<span class="dish-price">13,95 €</span></li>
      <li class="dish">Lenguado al Grill con Hierbas Provenzales.<span class="dish-price">20,75 €</span></li>
      <li class="dish">Pieza de Atún Fresco y su Salsa Griega.<span class="dish-price">18,95 €</span></li>
      <li class="dish">Lomo de Salmón con Salsa de Frambuesa.<span class="dish-price">11,25 €</span></li>
      <li class="dish">Parrillada de Pescado y Marisco.<span class="dish-price">23,505 €</span></li>
    </ul>
  </section>

  <section class="menu-section menu-section--kids">
    <h2 class="section-title">Especial Niños</h2>
    <ul class="dish-list">
      <li class="dish">Solomillo Junior, huevo y patatas fritas.<span class="dish-price">6,25 €</span></li>
      <li class="dish">Fish &amp; chips.<span class="dish-price">6,25 €</span></li>
    </ul>
  </section>
</main>
</body>
</html>
```